Mobile Friendly Lead Generation Landing Page

We are a web marketing company that specialized in web lead generation. Recently we have started buying media from mobile devices and we need a mobile interface(landing page) where we can collect user data in an effective manner.

Our current mobile landing page is:
http://www.tuitionscout.example.com/lp13d/index.aspx?a=true&source=581406
Through this you can see what the steps/questions users need to answer to get matched to a school. We need the design for the whole process.

We are pretty open for design ideas and our goal is to make this mobile optimized landing page have the look and feel of an app...but not an app.
There are several questions in the process but we are open to changing the way they are presented. As in, you can have one question at a time or a few.
The goal is to make this EXTREMELY EASY for users to interact with.

One example that we have liked is:
http://lessonhub.example/schools/47215-page1.lhub (please note that this opens only on mobile devices)

Some of these screenshots are attached.

Our web form looks like this:
http://www.tuitionscout.example.com/lp88/index.aspx?a=true

```html
<!DOCTYPE html>
<html lang="en">
<head>
<meta charset="utf-8">
<title>TuitionScout – Mobile Match Flow</title>
<link href="https://fonts.googleapis.com/css2?family=Roboto:wght@400;500;700&display=swap" rel="stylesheet">
<style>
  :root {
    --stage-dark: #2b2b2b;
    --stage-light: #5a5a5a;
    --screen-bg: #2a2d31;
    --green: #6cbd1a;
    --green-light: #8ed42b;
    --green-dark: #4f9412;
    --blue: #14ade0;
    --blue-dark: #0f86b8;
    --orange: #ff6600;
    --white: #ffffff;
    --outline: #3f8fae;
    --outline-soft: #c9cdd2;
  }
  * { box-sizing: border-box; margin: 0; padding: 0; }
  html, body { width: 1200px; height: 1000px; overflow: hidden; }
  body {
    background: radial-gradient(ellipse at 50% 55%, var(--stage-light) 0%, var(--stage-dark) 70%);
    font-family: "Roboto", Arial, sans-serif;
    color: var(--white);
    position: relative;
  }
  .screen {
    position: absolute;
    top: 186px;
    width: 354px;
    height: 632px;
    background: var(--screen-bg);
    overflow: hidden;
  }
  .screen--start { left: 198px; }
  .screen--progress { left: 652px; }

  .app-header {
    position: absolute; left: 0; top: 0; width: 100%; height: 64px;
    background: var(--green);
  }
  .screen--progress .app-header { background: var(--blue); height: 67px; }
  .brand {
    position: absolute; left: 30px; top: 0; height: 100%;
    display: flex; align-items: center;
    font-size: 24px; font-weight: 700; letter-spacing: -0.3px;
  }
  .header-divider {
    position: absolute; top: 0; left: 242px; width: 1px; height: 100%;
    background: rgba(0,0,0,0.15);
  }
  .progress-badge { position: absolute; left: 262px; top: 12px; }
  .progress-badge__text {
    position: absolute; left: 262px; top: 24px; width: 75px; text-align: center; line-height: 1;
  }
  .progress-value { font-size: 18px; font-weight: 700; display: block; }
  .progress-label { font-size: 12px; display: block; margin-top: 2px; }
  .progress-flat {
    position: absolute; left: 243px; top: 0; width: 111px; height: 67px;
    text-align: center; padding-top: 10px; line-height: 1;
  }
  .progress-flat .progress-value { font-size: 25px; }
  .progress-flat .progress-label { font-size: 16px; margin-top: 4px; }

  .ribbon { position: absolute; left: 0; top: 96px; }
  .ribbon__text {
    position: absolute; left: 42px; top: 96px; width: 270px; height: 40px;
    display: flex; align-items: center; justify-content: center; gap: 8px;
    font-size: 17px;
  }
  .ribbon__text strong { font-weight: 700; }

  .question {
    position: absolute; left: 15px; top: 169px;
    font-size: 16.5px;
  }
  .question b { font-weight: 700; margin-right: 6px; }

  .choice {
    position: absolute; left: 15px; width: 324px; height: 44px;
    border-radius: 3px;
    display: flex; align-items: center; justify-content: center;
    font-size: 18px; font-weight: 500;
    background: var(--blue);
  }
  .screen--progress .choice { left: 14px; background: var(--orange); font-size: 17px; }
  .choice--other {
    background: transparent !important;
    border: 1px solid var(--outline);
    font-weight: 400;
  }
  .screen--progress .choice--other { border-color: var(--outline-soft); font-weight: 500; }
  .choice__arrow { position: absolute; right: 12px; top: 13px; }

  .back-button {
    position: absolute; left: 15px; width: 324px; height: 44px;
    border-radius: 3px; background: var(--green);
    display: flex; align-items: center; justify-content: center;
    font-size: 18px;
  }
  .screen--progress .back-button { left: 14px; background: var(--blue); font-weight: 500; }
</style>
</head>
<body>

<!-- Step one: nothing answered yet -->
<section class="screen screen--start">
  <header class="app-header">
    <div class="brand">TuitionScout</div>
    <div class="header-divider"></div>
    <svg class="progress-badge" width="75" height="72" viewBox="0 0 75 72">
      <polygon points="0,0 75,0 75,54 37.5,72 0,54" fill="var(--blue-dark)"/>
      <polygon points="3,0 72,0 72,51 37.5,68 3,51" fill="var(--blue)"/>
    </svg>
    <div class="progress-badge__text">
      <span class="progress-value">0%</span>
      <span class="progress-label">complete</span>
    </div>
  </header>

  <svg class="ribbon" width="354" height="56" viewBox="0 0 354 56">
    <polygon points="14,14 62,14 62,54 14,54 30,34" fill="var(--green)"/>
    <polygon points="340,14 292,14 292,54 340,54 324,34" fill="var(--green)"/>
    <polygon points="42,40 62,40 62,54" fill="var(--green-dark)"/>
    <polygon points="312,40 292,40 292,54" fill="var(--green-dark)"/>
    <rect x="42" y="0" width="270" height="40" fill="var(--green-light)"/>
  </svg>
  <div class="ribbon__text">
    <span>Get matched in <strong>2 minutes</strong></span>
    <svg width="22" height="22" viewBox="0 0 22 22"><circle cx="11" cy="11" r="9" fill="none" stroke="#fff" stroke-width="2.2"/><path d="M11 6v5.5h4" fill="none" stroke="#fff" stroke-width="2.2"/></svg>
  </div>

  <p class="question"><b>1/10</b>Please select your field of interest</p>

  <div class="choice" style="top:207px">Art &amp; Design</div>
  <div class="choice" style="top:260px">Business</div>
  <div class="choice" style="top:313px">Criminal Justice</div>
  <div class="choice choice--other" style="top:366px">Other
    <svg class="choice__arrow" width="12" height="18" viewBox="0 0 12 18"><path d="M2 2l7 7-7 7" fill="none" stroke="#fff" stroke-width="2.4"/></svg>
  </div>

  <div class="back-button" style="top:569px">Back</div>
</section>

<!-- Progress state: partway through the flow -->
<section class="screen screen--progress">
  <header class="app-header">
    <div class="brand">TuitionScout</div>
    <div class="header-divider"></div>
    <div class="progress-flat">
      <span class="progress-value">65%</span>
      <span class="progress-label">complete</span>
    </div>
  </header>

  <svg class="ribbon" width="354" height="56" viewBox="0 0 354 56">
    <polygon points="14,14 62,14 62,54 14,54 30,34" fill="var(--green)"/>
    <polygon points="340,14 292,14 292,54 340,54 324,34" fill="var(--green)"/>
    <polygon points="42,40 62,40 62,54" fill="var(--green-dark)"/>
    <polygon points="312,40 292,40 292,54" fill="var(--green-dark)"/>
    <rect x="42" y="0" width="270" height="40" fill="var(--green-light)"/>
  </svg>
  <div class="ribbon__text">
    <span>Get matched in <strong>2 minutes</strong></span>
    <svg width="22" height="22" viewBox="0 0 22 22"><circle cx="11" cy="11" r="9" fill="none" stroke="#fff" stroke-width="2.2"/><path d="M11 6v5.5h4" fill="none" stroke="#fff" stroke-width="2.2"/></svg>
  </div>

  <p class="question" style="top:171px"><b>1/10</b>Please select your field of interest</p>

  <div class="choice" style="top:208px">Art &amp; Design</div>
  <div class="choice" style="top:262px">Art &amp; Design</div>
  <div class="choice" style="top:316px">Art &amp; Design</div>
  <div class="choice choice--other" style="top:372px">Other
    <svg class="choice__arrow" width="12" height="18" viewBox="0 0 12 18"><path d="M2 2l7 7-7 7" fill="none" stroke="var(--blue)" stroke-width="2.4"/></svg>
  </div>

  <div class="back-button" style="top:561px">Back</div>
</section>

</body>
</html>
```